Compelling Recycling & Environmental Product Awareness

Create a FB page design to engage target audiences that want to learn about plastic recycling facts and information. The product is expanded polystyrene (EPS) packaging which is highly recyclable while a majority of the public believes otherwise. We are looking to improve our credibility and increase traffic to our FB page. See https://www.brindlepost.example/KorvanLoop/

Target Market(s)

Primarily women ages 33-44; currently 68% of our current FB activity.

Industry/Entity Type

Plastic packaging industry.

Font styles to use
Sans Serif

Colors
0054AA
0677BA
7BADD7
CADEEF
E8F1F8
59FF00
82FF00
B8FF75
E3FFCB
F4FFEA
F0912C
F2A743
F7CA91
FBE8D2
FDF5EE

Requirements
Must have
• Visual engagement that promotes a persuasive presentation.
Should not have
• No hype.

```html
<!DOCTYPE html>
<html lang="en">
<head>
<meta charset="utf-8">
<title>Korvan Loop – EPS Recycling and Sustainability Cover</title>
<link rel="stylesheet" href="https://fonts.googleapis.com/css2?family=Rubik:wght@500;600;700&family=Quicksand:wght@600;700&display=swap">
<style>
  :root{
    --page-bg:#dfe9f1;
    --white:#ffffff;
    --steel-blue:#5c88a4;
    --earth-brown:#5a3022;
    --gold:#b8900f;
    --olive:#9aa61b;
    --orange:#f5a21e;
  }
  *{margin:0;padding:0;box-sizing:border-box}
  html,body{width:1200px;height:1081px;overflow:hidden;background:var(--page-bg)}
  .cover{
    position:absolute;left:0;top:318px;width:1200px;height:444px;overflow:hidden;
    box-shadow:0 10px 24px rgba(0,0,0,.25);
  }
  .cover-shapes{position:absolute;inset:0;width:100%;height:100%}
  .brand{
    position:absolute;left:54px;top:39px;display:flex;align-items:center;gap:10px;
  }
  .brand-mark{width:92px;height:92px;border-radius:50%;background:var(--gold)}
  .brand-name{
    font-family:'Rubik',sans-serif;font-weight:600;font-size:19px;line-height:1.05;color:var(--gold);width:110px;
  }
  .headline{
    position:absolute;right:623px;top:50px;text-align:right;white-space:nowrap;
    font-family:'Rubik',sans-serif;font-weight:700;color:var(--olive);letter-spacing:.5px;
  }
  .headline .line-one{font-size:35px;line-height:38px;display:block}
  .headline .line-two{font-size:28px;line-height:34px;display:block}
  .intro{
    position:absolute;left:52px;top:153px;width:480px;
    font-family:'Quicksand',sans-serif;font-weight:700;font-size:21.5px;line-height:28px;color:var(--white);letter-spacing:.3px;
  }
  .benefits-tag{
    position:absolute;left:54px;top:249px;width:146px;height:34px;border-radius:17px;
    background:var(--olive);color:var(--white);
    font-family:'Rubik',sans-serif;font-weight:700;font-size:19px;line-height:34px;text-align:center;letter-spacing:.5px;
  }
  .benefits-list{
    position:absolute;left:62px;top:288px;list-style:none;white-space:nowrap;
    font-family:'Rubik',sans-serif;font-weight:600;font-size:17.5px;line-height:24px;color:var(--white);
  }
  .benefits-list li{display:flex;align-items:center;gap:9px}
  .benefits-list svg{width:14px;height:14px;flex:none}
  .web-pill{
    position:absolute;left:809px;top:372px;width:344px;height:35px;border-radius:18px;
    background:var(--orange);color:var(--white);display:flex;align-items:center;justify-content:center;gap:12px;
    font-family:'Rubik',sans-serif;font-weight:700;font-size:20px;letter-spacing:.8px;white-space:nowrap;
  }
  .web-pill svg{width:20px;height:20px}
</style>
</head>
<body>
  <section class="cover">
    <svg class="cover-shapes" viewBox="0 0 1306 483" preserveAspectRatio="none">
      <defs>
        <linearGradient id="landscape" x1="0" y1="0" x2="0" y2="1">
          <stop offset="0" stop-color="#f3c98c"/>
          <stop offset=".45" stop-color="#f6dcb0"/>
          <stop offset=".68" stop-color="#8a6a55"/>
          <stop offset="1" stop-color="#6f8f3a"/>
        </linearGradient>
        <radialGradient id="symbol" cx=".5" cy=".5" r=".5">
          <stop offset="0" stop-color="#e6e6e6"/>
          <stop offset=".6" stop-color="#b9c07a"/>
          <stop offset="1" stop-color="#9aa61b"/>
        </radialGradient>
      </defs>
      <rect class="top-band" x="0" y="0" width="1306" height="157" fill="var(--white)"/>
      <rect class="intro-band" x="0" y="157" width="1306" height="130" fill="var(--steel-blue)"/>
      <rect class="benefits-band" x="0" y="287" width="1306" height="196" fill="var(--earth-brown)"/>
      <polygon class="gold-frame" points="698,0 1306,0 1306,483 700,483 764,380 510,345" fill="var(--gold)"/>
      <polygon role="img" aria-label="Photo of a wind turbine above mountain meadows at sunset" points="720,0 1306,0 1306,483 728,483 792,366 544,332" fill="url(#landscape)"/>
      <polygon class="orange-corner" points="1090,0 1306,0 1306,420" fill="var(--orange)"/>
      <ellipse role="img" aria-label="Recycling arrows surrounding white expanded polystyrene foam" cx="1105" cy="188" rx="145" ry="140" fill="url(#symbol)"/>
    </svg>

    <div class="brand">
      <span class="brand-mark"></span>
      <span class="brand-name">Korvan Loop Alliance</span>
    </div>

    <h1 class="headline">
      <span class="line-one">EPS RECYCLING</span>
      <span class="line-two">AND SUSTAINABILITY</span>
    </h1>

    <p class="intro">Expanded polystyrene (EPS) is a versatile, lightweight material that can be manufactured into a variety of products.</p>

    <div class="benefits-tag">BENEFITS</div>
    <ul class="benefits-list">
      <li><svg viewBox="0 0 14 14"><path d="M1 13C1 5 6 1 13 1C13 9 8 13 1 13Z" fill="var(--olive)"/></svg>Versatile &amp; Lightweight</li>
      <li><svg viewBox="0 0 14 14"><path d="M1 13C1 5 6 1 13 1C13 9 8 13 1 13Z" fill="var(--olive)"/></svg>Minimize Product Damage During Transit</li>
      <li><svg viewBox="0 0 14 14"><path d="M1 13C1 5 6 1 13 1C13 9 8 13 1 13Z" fill="var(--olive)"/></svg>Excellent Insulation Properties</li>
      <li><svg viewBox="0 0 14 14"><path d="M1 13C1 5 6 1 13 1C13 9 8 13 1 13Z" fill="var(--olive)"/></svg>Eligible for Electronics, Pharmaceuticals &amp; Food Shipments</li>
      <li><svg viewBox="0 0 14 14"><path d="M1 13C1 5 6 1 13 1C13 9 8 13 1 13Z" fill="var(--olive)"/></svg>EPS is Recyclable</li>
    </ul>

    <div class="web-pill">
      <svg viewBox="0 0 20 20" fill="none" stroke="var(--white)" stroke-width="1.6">
        <circle cx="10" cy="10" r="8.5"/>
        <ellipse cx="10" cy="10" rx="3.8" ry="8.5"/>
        <line x1="1.5" y1="10" x2="18.5" y2="10"/>
        <line x1="3" y1="5.5" x2="17" y2="5.5"/>
        <line x1="3" y1="14.5" x2="17" y2="14.5"/>
      </svg>
      <span>www.korvanloop.example</span>
    </div>
  </section>
</body>
</html>
```